Restaurant website built on Plimo’s responsive platform- No coding skills needed

We are looking to add to our company's website www.plimoweb.com a new inspiration page that will include examples of sites built using Plimo's platform.
In order to make it relevant, we would like to have multiple choices for every category, one of the categories is “restaurants.”

REQUIREMENTS:
o Build a "fake" restaurant site on Plimo’s responsive platform, no real restaurant information is needed. The site will include:
1. Homepage
• Restaurant header (no logo)
• Paragraph about the restaurant (can be Lorem ipsum)
• Contact details and contact buttons
• Tastr reviews
• Reserve-a-table widget
• Open hours
2. Menu page
• You can use any menu you'd like
• Reserve a table widget
• Photo gallery
3. Footer
• Social Media links
• Map with location of restaurant

* Order of the elements is up to the designer
* Designer may add more elements as they see fit
* Designer may alter elements from page to page
* Designer will define the site color pallet and text style

****Learn more on how to create a website on Plimo's platform here
https://clipzen.example/584203117

INSTRUCTIONS FOR THIS PROJECT:
Register for a 30-day free trial for Pro access to the platform:
http://www.plimoweb.com/plimopro?_pw_referral=GrfHub

a. After registering, access the dashboard and click on “Create Responsive Website.”
b. Choose a template
c. Start editing! .
d. No need to publish. When ready, take a screenshot of the preview and submit the screenshot to this GraphicHub project. Include the URL/Link to the preview within the submission description.
e. For more information on Plimo, visit the support page at https://support.plimoweb.com/02PlimoOne/Quick_Guide OR call our Support line Mon.-Fri., 9AM-9PM ET.1-866-555-0193

DESIGN PREFERENCES
freestyle (not related to the Plimo brand)

DESIGN SAMPLES (for inspiration)
http://www.plimoweb.com/responsive-website/templates

What not to include in the design -
no restrictions

DELIVERABLES:
* Website on Plimo (No PSD. No coding needed)
* Screenshot preview to GraphicHub with URL/link to your site’s preview.

ABOUT THE COMPANY:
Plimo is a website builder based in California that allow designers, web designers and practically anyone to build its own site. No development and/or technical skills required.

NOTE:
* Plimo is an external site and is not part of GraphicHub
* Please refer to Plimo's Terms and Conditions for information regarding how submissions will be handled (http://www.plimoweb.com/legal/terms)

Target Market(s)

SMBs and web designers that want to create simple, professional and beautiful websites

Industry/Entity Type

Restaurant

Number of Pages Required

2 page

Requirements
Must have
• Please send a preview of the site you created on Plimo, NOT a PSD/JPEG
Should not have
• No coding skills are needed- any web designer can build a site on Plimo

```html
<!DOCTYPE html>
<html lang="en">
<head>
<meta charset="utf-8">
<title>Restaurant Site</title>
<link href="https://fonts.googleapis.com/css2?family=Lobster&family=Raleway:wght@400;500;600;700&family=Source+Sans+3:wght@400;600;700&display=swap" rel="stylesheet">
<style>
:root{
  --brown:#3a0d05;
  --white:#ffffff;
  --ink:#3a0d05;
  --text:#6b6b6b;
  --field:#f0f0f0;
  --star:#e0332b;
  --link:#3fa7d6;
  --foot:#efefef;
  --rule:#6b3a2e;
}
*{box-sizing:border-box;margin:0;padding:0}
html,body{width:1200px;height:2428px;overflow:hidden;background:var(--white)}
body{position:relative;font-family:"Raleway",sans-serif;color:var(--text)}
.abs{position:absolute}

.topbar{left:0;top:0;width:1200px;height:55px;background:var(--brown)}
.brand{left:26px;top:16px;display:flex;align-items:center;gap:10px;color:var(--white);font-size:15px;font-weight:500;letter-spacing:.5px}
.brand-dot{width:22px;height:22px;border-radius:50%;border:2px solid var(--white)}
.social{right:26px;top:17px;display:flex;gap:8px}
.social span{width:20px;height:20px;border-radius:50%;border:2px solid var(--white)}

.hero{left:0;top:55px;width:1200px;height:427px;
  background:
    radial-gradient(ellipse 180px 300px at 1110px 200px,rgba(220,40,30,.85),rgba(220,40,30,0) 70%),
    linear-gradient(180deg,#7a4a2a 0%,#9a6a45 18%,#6fa0c4 38%,#2f6f9e 58%,#6a4a32 78%,#3b2417 100%)}
.hero-title{left:0;top:118px;width:1200px;text-align:center;font-family:"Lobster",cursive;font-size:56px;line-height:66px;color:var(--white)}
.hero-sub{left:0;top:256px;width:1200px;text-align:center;font-size:17px;color:var(--white)}
.search-input{left:400px;top:297px;width:400px;height:32px;border:2px solid var(--white);background:rgba(0,0,0,.12);color:var(--white);font-size:14px;padding:6px 10px}
.search-btn{left:668px;top:344px;width:132px;height:34px;background:var(--brown);color:var(--white);font-family:"Source Sans 3",sans-serif;font-weight:700;font-size:15px;text-align:center;line-height:34px}

.navbar{left:0;top:482px;width:1200px;height:52px;background:var(--brown)}
.nav-item{top:502px;color:var(--white);font-size:11px;font-weight:600;letter-spacing:1px}
.nav-badge{left:504px;top:436px;width:142px;height:142px;border-radius:50%;background:var(--white);border:6px solid #e4e4e4;display:flex;align-items:center;justify-content:center;text-align:center;font-family:"Source Sans 3",sans-serif;font-weight:700;font-size:15px;line-height:19px;color:var(--brown);letter-spacing:1px}

.about-photo{left:300px;top:587px;width:120px;height:120px;border-radius:50%;background:radial-gradient(circle at 50% 40%,#f6dc8a,#e3a14a 60%,#c97a35)}
.about-title{left:459px;top:590px;font-family:"Source Sans 3",sans-serif;font-size:21px;font-weight:400;color:var(--ink);letter-spacing:.5px}
.about-text{left:459px;top:632px;width:440px;font-size:10.5px;line-height:18px;color:var(--text)}

.food-band{left:0;top:757px;width:1200px;height:269px;
  background:
    radial-gradient(ellipse 260px 120px at 900px 190px,rgba(60,30,20,.9),rgba(60,30,20,0) 75%),
    radial-gradient(ellipse 160px 90px at 340px 120px,rgba(200,140,70,.9),rgba(200,140,70,0) 75%),
    linear-gradient(100deg,#e9e6e2 0%,#8a5a32 30%,#b38a5a 55%,#6a4a32 80%,#e6e2dc 100%)}

.section-title{left:0;width:1200px;text-align:center;font-family:"Source Sans 3",sans-serif;font-size:27px;font-weight:400;color:var(--ink);letter-spacing:1px}
.field-label{top:1093px;width:188px;text-align:center;font-size:10px;color:var(--text);letter-spacing:.5px}
.field{top:1109px;height:30px;background:var(--field);font-size:14px;color:#333;text-align:center;line-height:30px}
.send-btn{left:724px;top:1169px;width:176px;height:32px;background:var(--brown);color:var(--white);font-weight:700;font-size:12px;letter-spacing:1px;text-align:center;line-height:32px}

.gallery{left:0;top:1279px;width:1200px;height:529px;display:grid;grid-template-columns:repeat(3,1fr);grid-template-rows:repeat(2,1fr);gap:2px}
.tile:nth-child(1){background:radial-gradient(ellipse at 40% 70%,#f1e6cf,#c9935a 55%,#7a4a22)}
.tile:nth-child(2){background:radial-gradient(ellipse 70% 40% at 50% 75%,#f1eee9,#c99a5a 50%,#2a1a12)}
.tile:nth-child(3){background:radial-gradient(ellipse 70% 40% at 55% 70%,#f4f1ec,#9c8470 50%,#3a2e28)}
.tile:nth-child(4){background:radial-gradient(ellipse at 60% 60%,#6d8d3a,#a35b36 45%,#f3efe9)}
.tile:nth-child(5){background:radial-gradient(ellipse 60% 40% at 40% 80%,#ece7e1,#7a3a2a 50%,#2b1510)}
.tile:nth-child(6){background:radial-gradient(ellipse 80% 40% at 50% 45%,#e8b54f,#8a5a1f 50%,#1e1208)}

.map{left:0;top:1868px;width:1200px;height:227px;background:linear-gradient(120deg,#cfe3f2 0%,#ede9dc 30%,#a9cde6 50%,#ece7da 70%,#d8e6d0 100%)}

.footer{left:0;top:2095px;width:1200px;height:285px;background:var(--brown)}
.open-sign{left:304px;top:2111px;width:182px;height:95px;background:linear-gradient(180deg,#e24a3b,#b5211a);border-radius:4px}
.hours-title{left:300px;top:2231px;font-family:"Source Sans 3",sans-serif;font-weight:700;font-size:24px;color:var(--white)}
.hours-row{left:300px;top:2280px;width:192px;display:flex;justify-content:space-between;font-size:10px;color:var(--white);padding-bottom:10px;border-bottom:1px solid var(--rule)}

.reviews-head{left:508px;top:2113px;display:flex;align-items:baseline;gap:6px;color:var(--white);font-family:"Source Sans 3",sans-serif}
.reviews-head .src{font-size:11px;font-weight:700}
.reviews-head .ttl{font-size:26px;font-weight:400}
.stars{display:flex;gap:1px}
.stars i{width:9px;height:9px;background:var(--star);display:block}
.review{left:508px;width:392px;display:flex;gap:12px}
.avatar{width:64px;height:64px;flex:none;background:linear-gradient(180deg,#8a7a70,#c9b8aa);border-radius:2px}
.review-meta{display:flex;gap:16px;font-size:8px;color:var(--white);margin-bottom:4px}
.review-body{font-size:9.5px;line-height:15px;color:#e8dcd8;margin-top:8px}
.more{left:508px;top:2350px;font-size:10px;font-weight:700;color:var(--link)}
.review-rule{left:508px;top:2342px;width:392px;height:1px;background:var(--rule)}

.bottombar{left:0;top:2380px;width:1200px;height:48px;background:var(--foot);text-align:center;line-height:48px;font-size:11px;color:#666}
.bottombar u{color:#555}
</style>
</head>
<body>

<header class="abs topbar"></header>
<div class="abs brand"><span class="brand-dot"></span>RESTAURANT SITE</div>
<div class="abs social" aria-label="Social media links"><span></span><span></span><span></span></div>

<section class="abs hero" role="img" aria-label="Beachside restaurant terrace with wooden beams overlooking the sea"></section>
<h1 class="abs hero-title">Where you want to<br>dineout today</h1>
<p class="abs hero-sub">Search For your nearest Restaurant</p>
<div class="abs search-input">type your keywords here</div>
<div class="abs search-btn">Search Now</div>

<nav class="abs navbar"></nav>
<span class="abs nav-item" style="left:328px">RESTAURANTS</span>
<span class="abs nav-item" style="left:443px">MENU</span>
<span class="abs nav-item" style="left:674px">LOCATIONS</span>
<span class="abs nav-item" style="left:769px">ABOUT</span>
<div class="abs nav-badge">RESTAURANT<br>SITE</div>

<div class="abs about-photo" role="img" aria-label="Round photo of a sunlit field"></div>
<h2 class="abs about-title">WHO WE ARE</h2>
<p class="abs about-text">This is a paragraph. Writing in paragraphs lets your visitor find what they are looking for quickly and easily. Make sure your titles stand out from the rest of the text. This is a paragraph. Writing in paragraphs lets your visitor find what they are looking for quickly and easily. Make sure your titles stand out from the rest of the text.</p>

<div class="abs food-band" role="img" aria-label="Grilled steak and fritters served on a wooden board"></div>

<h2 class="abs section-title" style="top:1049px">RESERVE A TABLE</h2>
<span class="abs field-label" style="left:300px">DATE</span>
<span class="abs field-label" style="left:506px">TIME</span>
<span class="abs field-label" style="left:712px">RESTAURANT</span>
<div class="abs field" style="left:300px;width:188px">06/09/2015</div>
<div class="abs field" style="left:508px;width:184px"></div>
<div class="abs field" style="left:712px;width:188px"></div>
<div class="abs send-btn">SEND</div>

<h2 class="abs section-title" style="top:1231px">PHOTO GALLERY</h2>
<div class="abs gallery">
  <div class="tile" role="img" aria-label="Dining room with set tables"></div>
  <div class="tile" role="img" aria-label="Chicken burger on a plate"></div>
  <div class="tile" role="img" aria-label="Plated dish with wine glasses"></div>
  <div class="tile" role="img" aria-label="Fresh salads and small dishes"></div>
  <div class="tile" role="img" aria-label="Wine being poured at a candlelit table"></div>
  <div class="tile" role="img" aria-label="Warmly lit buffet counter"></div>
</div>

<h2 class="abs section-title" style="top:1820px">OUR LOCATION</h2>
<div class="abs map" role="img" aria-label="Street map showing the restaurant location"></div>

<footer class="abs footer"></footer>
<div class="abs open-sign" role="img" aria-label="Hanging open sign"></div>
<h3 class="abs hours-title">Business Hours</h3>
<div class="abs hours-row"><span>Sun - Sat</span><span>9:00 - 17:00</span></div>

<div class="abs reviews-head"><span class="src">Tastr</span><span class="ttl">Reviews</span></div>
<div class="abs stars" style="left:855px;top:2158px"><i></i><i></i><i></i><i></i><i></i></div>

<div class="abs review" style="top:2170px">
  <div class="avatar" role="img" aria-label="Reviewer avatar"></div>
  <div>
    <div class="review-meta"><span>Nora S.</span><span>03/10/2015</span></div>
    <div class="stars"><i></i><i></i><i></i><i></i><i></i></div>
    <p class="review-body">Tastr got this one right! We finished up our Harbor Island tour today and I just wanted fish and chips. That's all I wanted! So we walked over to check it out...</p>
  </div>
</div>

<div class="abs review" style="top:2259px">
  <div class="avatar" role="img" aria-label="Reviewer avatar"></div>
  <div>
    <div class="review-meta"><span>Simon J.</span><span>02/25/2015</span></div>
    <div class="stars"><i></i><i></i><i></i><i></i><i></i></div>
    <p class="review-body">Waited one hour for a basket of fish and chips. Worth trying but not worth doing again. Definitely fresh and high quality. The fries are great. Nothing...</p>
  </div>
</div>
<div class="abs review-rule"></div>
<span class="abs more">Read more on Tastr.com &gt;&gt;</span>

<div class="abs bottombar">Contact us: <u>hello@restaurantsite.example</u></div>

</body>
</html>
```